Varnel Strategic Property Logo & Business card design brief

Dear Sir/Madam,

I need to have a logo design incorporated into a business card layout so as to then have these formatted files available to me to then take to printers for print production. Am I right to believe that this design task from start to finish can be turned around in 5 days and please clarify if these 5 days incorporate the weekend?

Fyi I wish the logo colours to be a bright burnt orange and vivid azure blue like the ocean on a clear day - I have these colours on a JPEG image that I can email the successful tendering / competition wining design party. Additionally I'd like to incorporate a proportionately scaled simplified earth globe orientating towards Australia and SE Asia - showing prominately Southern China. This globe can either be stand alone &/or incorporated into the Varnel brand mark. Some gold colour gilding on say the meridian lines would look striking and distinctive.

Nb - the reverse side of the business card will simply have our Hong Kond office address details in Chinese Characters

Put simply, I want our logo and business card layout to look elegant, classy and classic without being too hip &/or trendy. Although this is a new start up company I want the look and feel to be like an established and venerated brand that sits proudly amongst professional positioned financial groups and organisations which are our cleintele.

Looking forward to working with your organisation to achieve this task and revealing the winner on Monday. For precise guidance purposes I can forward preferred colour palate for final artwork finesse .

Regards Greg - Sales & Marketing Director
Varnel Property Group
Melbourne , Australia

Target Market(s)

Professional investor high net work individuals . Companies and managed investment funds looking to invest into Australian property developments

Industry/Entity Type

Property Management

Contact Information for Business Card

Level 4, 288 Brompwell Rd,
Melbourne, Vic 3187. | Australia

Font styles to use
Serif

Colors
0555a3
f37122

Requirements
Must have
• A professional elegant and classy look and feel to the overall brand mark and type face . Classic fonts over trendy hip styles would be preferred. For guidance purposes look at major global banks and investment companies
Nice to have
• Being a property development group and for positioning purposes we
• Require a assic yet innovative feel here is to achieve the balance
Should not have
• The actual company name and address details can be black on white background , but within the actual logo design & the accompanying globe with the meridian lines please DO NOT use white & black in this component of the brand mark

```html
<!DOCTYPE html>
<html lang="en">
<head>
<meta charset="utf-8">
<title>Varnel Strategic Property – Business Card</title>
<link rel="stylesheet" href="https://fonts.googleapis.com/css2?family=Open+Sans:wght@400;600;700&display=swap">
<style>
  :root {
    --azure: #0555a3;
    --burnt-orange: #f37122;
    --ink: #1f1f1f;
    --card: #ffffff;
    --backdrop: #e9e7e3;
  }
  * { margin: 0; padding: 0; box-sizing: border-box; }
  html, body {
    width: 1200px;
    height: 900px;
    overflow: hidden;
    background: var(--backdrop);
    font-family: "Open Sans", Arial, sans-serif;
  }
  .canvas {
    position: relative;
    width: 1200px;
    height: 900px;
  }
  .card {
    position: absolute;
    left: 250px;
    width: 700px;
    height: 400px;
    background: var(--card);
    box-shadow: 0 4px 14px rgba(0,0,0,0.15);
    overflow: hidden;
  }
  .card--front { top: 40px; }
  .card--back { top: 470px; }

  .brand {
    position: absolute;
    display: flex;
    align-items: center;
    gap: 16px;
    color: var(--azure);
    font-weight: 600;
  }
  .brand__dot {
    width: 58px;
    height: 58px;
    border-radius: 50%;
    background: var(--azure);
    flex: none;
  }
  .brand__name { display: flex; flex-direction: column; line-height: 1; }
  .brand__word { font-size: 52px; letter-spacing: 3px; }
  .brand__tagline { font-size: 25px; margin-top: 6px; letter-spacing: 0.5px; }

  .card--front .brand { left: 170px; top: 138px; }
  .card--back .brand { left: 360px; top: 150px; }
  .card--back .brand__dot { width: 48px; height: 48px; }
  .card--back .brand__word { font-size: 42px; }
  .card--back .brand__tagline { font-size: 20px; }

  .corner-mark { position: absolute; left: 0; top: 0; }

  .holder { position: absolute; left: 74px; top: 22px; }
  .holder__name {
    color: var(--burnt-orange);
    font-weight: 700;
    font-size: 19px;
  }
  .holder__title {
    color: var(--ink);
    font-size: 15px;
    margin-top: 2px;
  }

  .contact {
    position: absolute;
    left: 32px;
    top: 160px;
    color: var(--ink);
    font-size: 15px;
    line-height: 1.45;
    list-style: none;
  }
  .contact__address { margin-bottom: 4px; }
  .contact__item { display: flex; align-items: center; gap: 10px; }
  .contact__icon { width: 13px; height: 13px; flex: none; }

  .bands { position: absolute; left: 0; top: 0; }
</style>
</head>
<body>
<main class="canvas">

  <section class="card card--front" aria-label="Card front">
    <div class="brand">
      <span class="brand__dot"></span>
      <span class="brand__name">
        <span class="brand__word">VARNEL</span>
        <span class="brand__tagline">Strategic property</span>
      </span>
    </div>
  </section>

  <section class="card card--back" aria-label="Card back">
    <svg class="corner-mark" width="60" height="50" viewBox="0 0 60 50">
      <polygon points="0,8 24,8 0,36" fill="var(--burnt-orange)"/>
      <polygon points="32,8 58,8 58,42 4,42" fill="var(--azure)"/>
    </svg>

    <div class="holder">
      <p class="holder__name">Dorian K P Hale</p>
      <p class="holder__title">Director International Capital Flow</p>
    </div>

    <ul class="contact">
      <li class="contact__address">Level 4, 288 Brompwell Rd,<br>Melbourne, Vic 3187. | Australia</li>
      <li class="contact__item">
        <svg class="contact__icon" viewBox="0 0 12 12"><rect x="3" y="0.5" width="6" height="11" rx="1.2" fill="none" stroke="var(--burnt-orange)" stroke-width="1.4"/><circle cx="6" cy="9.5" r="0.8" fill="var(--burnt-orange)"/></svg>
        +(852) 5550 1842
      </li>
      <li class="contact__item">
        <svg class="contact__icon" viewBox="0 0 12 12"><rect x="0.5" y="2" width="11" height="8" fill="var(--burnt-orange)"/><polyline points="0.5,2 6,6.5 11.5,2" fill="none" stroke="#fff" stroke-width="1"/></svg>
        dkhcapital27@mailbox.com
      </li>
      <li class="contact__item">
        <svg class="contact__icon" viewBox="0 0 12 12"><circle cx="6" cy="6" r="5.5" fill="var(--burnt-orange)"/><path d="M1 6h10M6 0.5c-2.5 3-2.5 8 0 11M6 0.5c2.5 3 2.5 8 0 11" fill="none" stroke="#fff" stroke-width="0.8"/></svg>
        www.varnel.com.au
      </li>
    </ul>

    <svg class="bands" width="700" height="400" viewBox="0 0 700 400">
      <polygon points="0,290 285,290 268,322 0,322" fill="var(--burnt-orange)"/>
      <polygon points="297,300 700,300 700,400 244,400" fill="var(--azure)"/>
    </svg>

    <div class="brand">
      <span class="brand__dot"></span>
      <span class="brand__name">
        <span class="brand__word">VARNEL</span>
        <span class="brand__tagline">Strategic property</span>
      </span>
    </div>
  </section>

</main>
</body>
</html>
```